Business Card Design for Consulting Company

I require a Business Card design for my Consulting company. <br/><br/>My company name is: Marek Olvani Consulting Inc.<br/>My website is: www.marekolvaniconsulting.example<br/><br/>My company focuses on management and software development for the Tallobrix CRM platform (www.tallobrix.example)<br/><br/>I have a logo already designed...see attached.
Updates

Also Include my Name and Title: Marek T.L. Olvani President

Target Market(s)

Tallobrix Customers

Contact Information for Business Card

Only include my LOGO (provided)
My Name: Marek TL Olvani
My Title: President
My Company Name: Marek Olvani Consulting Inc.
My Website: www.marekolvaniconsulting.example
My Email: marek.olvani.consulting@mailbox.example

NO PHONE NUMBER
NO ADDRESS

Font styles to use
Serif
Sans Serif
Other font styles liked:
• see my website: www.marekolvaniconsulting.example

Colors

Designer to choose colors to be used in the design.

Requirements
Must have
• Must include my Orange
• Include my name (Marek T.L. Olvani), title (President) company name, website and email
• It should also have a tag line like: Tallobrix Consulting
• I'm flexible with the tag line
Should not have
• Don't include my phone number or address

```html
<!DOCTYPE html>
<html lang="en">
<head>
<meta charset="utf-8">
<title>Marek Olvani Consulting Inc. — Business Card</title>
<link rel="stylesheet" href="https://fonts.googleapis.com/css2?family=Roboto:wght@400;700&display=swap">
<style>
  :root {
    --backdrop: #cfcfcf;
    --card: #1f1f1f;
    --card-edge: #2a2a2a;
    --orange: #f0871e;
    --ink: #ececec;
    --ink-soft: #c9c9c9;
  }
  * { margin: 0; padding: 0; box-sizing: border-box; }
  html, body {
    width: 1200px;
    height: 675px;
    overflow: hidden;
    background: var(--backdrop);
    font-family: "Roboto", Arial, sans-serif;
  }
  .canvas {
    width: 1200px;
    height: 675px;
    display: flex;
    align-items: center;
    justify-content: center;
    gap: 40px;
  }
  .card {
    width: 520px;
    height: 297px;
    background: linear-gradient(160deg, var(--card-edge), var(--card) 60%);
    border-radius: 40px 0 40px 0;
    box-shadow: 0 10px 24px rgba(0,0,0,0.25);
    position: relative;
  }

  /* Wordmark standing in for the client mark */
  .wordmark {
    display: flex;
    align-items: center;
    gap: 10px;
    color: var(--orange);
    font-weight: 700;
    white-space: nowrap;
  }
  .wordmark-square {
    width: 14px;
    height: 14px;
    background: var(--orange);
    flex: none;
  }

  /* Front */
  .card-front {
    display: flex;
    align-items: center;
    padding: 0 30px 0 36px;
  }
  .card-front .wordmark { font-size: 19px; width: 150px; }
  .card-front .wordmark-square { width: 10px; height: 10px; }
  .divider {
    width: 1px;
    height: 150px;
    background: var(--orange);
    margin: 0 18px 0 14px;
    flex: none;
  }
  .details { flex: 1; }
  .person-name {
    color: var(--orange);
    font-weight: 700;
    font-size: 19px;
  }
  .person-title {
    color: var(--ink);
    font-weight: 400;
    font-size: 10px;
    margin-left: 6px;
  }
  .rule {
    height: 1px;
    background: var(--ink-soft);
    margin: 8px 0;
    opacity: 0.6;
  }
  .rule-orange { background: var(--orange); opacity: 1; }
  .company-name {
    color: var(--ink);
    font-size: 16px;
  }
  .contact-list {
    list-style: none;
    font-size: 11px;
    line-height: 1.55;
    color: var(--ink);
  }
  .contact-label { color: var(--orange); }

  /* Back */
  .card-back {
    display: flex;
    flex-direction: column;
    align-items: center;
    justify-content: center;
    gap: 14px;
  }
  .card-back .wordmark { font-size: 34px; }
  .tagline {
    color: var(--orange);
    font-size: 15px;
    letter-spacing: 0.5px;
  }
</style>
</head>
<body>
<main class="canvas">
  <section class="card card-front" aria-label="Business card front">
    <div class="wordmark">
      <span class="wordmark-square"></span>
      <span>Marek Olvani</span>
    </div>
    <div class="divider"></div>
    <div class="details">
      <p><span class="person-name">Marek TL Olvani</span><span class="person-title">( President )</span></p>
      <div class="rule"></div>
      <p class="company-name">Marek Olvani Consulting Inc.</p>
      <div class="rule rule-orange"></div>
      <ul class="contact-list">
        <li><span class="contact-label">Email:</span> marek.olvani.consulting@mailbox.example</li>
        <li><span class="contact-label">Website:</span> www.marekolvaniconsulting.example</li>
      </ul>
    </div>
  </section>

  <section class="card card-back" aria-label="Business card back">
    <div class="wordmark">
      <span class="wordmark-square"></span>
      <span>Marek Olvani</span>
    </div>
    <p class="tagline">Tallobrix Consulting</p>
  </section>
</main>
</body>
</html>
```